Clever & creative business card needed for a pediatric dentist.

We need a business card for a pediatric dentist that is building a brand-new pediatric dental practice. He is funny, outgoing, and sociable, and he hopes to give his business card to dentists and pediatricians so that he can give them information of where to refer infants, children, and teenagers that need high quality and attainable dental care.

The name of the dental practice is Copper Fern Pediatric Dentistry. Logo design .png / .pdf/ .jpg are provided to aid in the design.

The dentist's last name is Tolvan (which sounds like "burger", as in "hamburger” or “cheeseburger"). Since it is pediatric practice, kudos will be given to designs that implement a little joke into the design - but hopefully in a small or hidden way (such as putting something like a cheeseburger on the back of the card, or hiding it an an abstract way).

Thank you!

Please make a design that incorporates colors. It should be fun! Not too serious. It does not have to follow the color scheme of the logos.

```html
<!DOCTYPE html>
<html lang="en">
<head>
<meta charset="utf-8">
<title>Copper Fern Pediatric Dentistry – Business Card</title>
<link href="https://fonts.googleapis.com/css2?family=Dancing+Script:wght@700&family=Signika:wght@400;500&display=swap" rel="stylesheet">
<style>
  :root {
    --page-bg: #e9e5df;
    --card-light: #b9dcb3;
    --card-mid: #a3cf9d;
    --card-dark: #7ea978;
    --panel-light: rgba(235, 245, 232, 0.55);
    --name-green: #2f7d3b;
    --ink: #34453a;
    --ink-soft: #3f5446;
    --brand-ink: #1f2a22;
    --burger-top: #5f7f5c;
    --burger-bottom: #4a6448;
  }
  * { margin: 0; padding: 0; box-sizing: border-box; }
  html, body {
    width: 1200px;
    height: 969px;
    overflow: hidden;
    background: var(--page-bg);
  }
  .canvas {
    position: relative;
    width: 1200px;
    height: 969px;
  }
  .card {
    position: absolute;
    left: 57px;
    top: 175px;
    width: 1085px;
    height: 619px;
    overflow: hidden;
    background: linear-gradient(100deg, var(--card-light) 0%, var(--card-mid) 45%, var(--card-dark) 100%);
    box-shadow: 0 10px 30px rgba(0,0,0,0.18);
    font-family: "Signika", sans-serif;
    color: var(--ink);
  }
  .brand-panel {
    position: absolute;
    left: 395px;
    top: 0;
    width: 660px;
    height: 619px;
    border-radius: 48% 48% 40% 40% / 38% 38% 60% 60%;
    background: radial-gradient(ellipse at 50% 40%, var(--panel-light), rgba(235,245,232,0.15) 70%, transparent 100%);
  }
  .burger {
    position: absolute;
    border-radius: 46% 46% 38% 38%;
    background: linear-gradient(180deg, var(--burger-top) 0%, var(--burger-top) 55%, var(--burger-bottom) 56%, var(--burger-bottom) 100%);
  }
  .burger--top-left { left: 17px; top: 24px; width: 95px; height: 90px; }
  .burger--bottom-right { left: 877px; top: 489px; width: 118px; height: 110px; }

  .person {
    position: absolute;
    left: 54px;
    top: 118px;
  }
  .person__name {
    font-family: "Dancing Script", cursive;
    font-weight: 700;
    font-size: 60px;
    line-height: 1;
    color: var(--name-green);
  }
  .person__title {
    margin: 4px 0 0 25px;
    font-size: 31px;
    font-weight: 500;
    color: var(--brand-ink);
  }
  .address {
    position: absolute;
    left: 53px;
    top: 252px;
    font-size: 25px;
    line-height: 30px;
    color: var(--ink-soft);
  }
  .contacts {
    position: absolute;
    left: 53px;
    top: 332px;
    list-style: none;
    font-size: 26px;
    line-height: 31px;
    color: var(--ink-soft);
  }
  .contacts li { display: flex; align-items: center; }
  .contacts svg { width: 20px; height: 20px; margin-right: 15px; fill: var(--ink-soft); }

  .brand {
    position: absolute;
    left: 520px;
    top: 240px;
    width: 420px;
    text-align: center;
    color: var(--brand-ink);
    font-weight: 500;
  }
  .brand__dot {
    width: 110px;
    height: 110px;
    margin: 0 auto 22px;
    border-radius: 50%;
    background: var(--name-green);
  }
  .brand__name {
    font-size: 58px;
    line-height: 1;
  }
  .brand__sub {
    margin-top: 10px;
    font-size: 21px;
    letter-spacing: 5px;
  }
</style>
</head>
<body>
<div class="canvas">
  <section class="card">
    <div class="brand-panel"></div>

    <div class="burger burger--top-left" role="img" aria-label="Small smiling cheeseburger illustration"></div>

    <div class="person">
      <h1 class="person__name">Owen Tolvan</h1>
      <p class="person__title">Pediatrician</p>
    </div>

    <address class="address">4210 Larkspur Way<br>Juneau, Alaska 99801</address>

    <ul class="contacts">
      <li><svg viewBox="0 0 24 24"><path d="M6.6 10.8a15.1 15.1 0 0 0 6.6 6.6l2.2-2.2c.3-.3.7-.4 1-.2 1.1.4 2.3.6 3.6.6.6 0 1 .4 1 1V20c0 .6-.4 1-1 1A17 17 0 0 1 3 4c0-.6.4-1 1-1h3.5c.6 0 1 .4 1 1 0 1.3.2 2.5.6 3.6.1.3 0 .7-.2 1z"/></svg>555-204-1187</li>
      <li><svg viewBox="0 0 24 24"><path d="M7 1h10a2 2 0 0 1 2 2v18a2 2 0 0 1-2 2H7a2 2 0 0 1-2-2V3a2 2 0 0 1 2-2zm0 3v14h10V4z"/></svg>555-318-6642</li>
      <li><svg viewBox="0 0 24 24"><path d="M6 2h12v5H6zM3 8h18a2 2 0 0 1 2 2v7h-4v5H5v-5H1v-7a2 2 0 0 1 2-2zm4 8v4h10v-4z"/></svg>555-472-9035</li>
      <li><svg viewBox="0 0 24 24"><path d="M2 5h20v14H2zm2 2v.5l8 5 8-5V7z"/></svg>hello@copperfern.com</li>
      <li><svg viewBox="0 0 24 24"><path d="M12 2a10 10 0 1 0 0 20 10 10 0 0 0 0-20zm-1 17.9A8 8 0 0 1 4.1 11L9 16v1a2 2 0 0 0 2 2zm6.9-2.5A2 2 0 0 0 16 16h-1v-3a1 1 0 0 0-1-1H8v-2h2a1 1 0 0 0 1-1V7h2a2 2 0 0 0 2-2v-.4a8 8 0 0 1 2.9 12.8z"/></svg>www.copperfern.com</li>
    </ul>

    <div class="brand">
      <div class="brand__dot"></div>
      <p class="brand__name">copper fern</p>
      <p class="brand__sub">PEDIATRIC DENTISTRY</p>
    </div>

    <div class="burger burger--bottom-right" role="img" aria-label="Smiling cheeseburger illustration"></div>
  </section>
</div>
</body>
</html>
```